Harmony Four Showcase
Date: Sunday Oct 2, 2022
When: 2-4 p.m.
Location: Brindle9 Alehouse
413 Marigold Wy #200, Sacramento, CA 95821
Tickets: www.Ticketwisp.example
General seating: $15 for adults and $10 for students

```html
<!DOCTYPE html>
<html lang="en">
<head>
<meta charset="utf-8">
<title>Harmony Four Showcase</title>
<link rel="stylesheet" href="https://fonts.googleapis.com/css2?family=Bebas+Neue&family=Gloock&family=Montserrat:wght@400;500;800;900&display=swap">
<style>
  :root {
    --ink: #111111;
    --black: #000000;
    --white: #ffffff;
    --red: #e8111a;
    --red-deep: #c9070f;
    --stage-pink: #f1a7d8;
    --stage-magenta: #d05fb4;
    --stage-amber: #c86a2c;
    --crowd-brown: #3a1a10;
  }
  * { box-sizing: border-box; margin: 0; padding: 0; }
  html, body { width: 765px; height: 1200px; overflow: hidden; background: var(--white); }
  .flyer {
    position: relative;
    width: 765px;
    height: 1200px;
    background: var(--black);
    overflow: hidden;
    font-family: "Montserrat", Arial, sans-serif;
  }
  .concert-photo {
    position: absolute;
    left: 0; top: 0;
    width: 765px; height: 800px;
    background:
      radial-gradient(ellipse 60% 30% at 50% 30%, rgba(255,230,240,0.75), rgba(255,230,240,0) 70%),
      linear-gradient(180deg,
        var(--stage-magenta) 0%,
        var(--stage-pink) 18%,
        #e79bc6 32%,
        var(--stage-amber) 52%,
        var(--crowd-brown) 70%,
        var(--black) 100%);
  }
  .event-title {
    position: absolute;
    left: 0; top: 82px;
    width: 765px;
    text-align: center;
    font-family: "Gloock", Georgia, serif;
    font-weight: 400;
    font-size: 80px;
    line-height: 82px;
    letter-spacing: 2px;
    color: var(--ink);
  }
  .event-day {
    position: absolute;
    left: 0; top: 680px;
    width: 765px;
    text-align: center;
    font-weight: 900;
    font-size: 66px;
    line-height: 66px;
    color: var(--red);
  }
  .event-date {
    position: absolute;
    left: 0; top: 744px;
    width: 765px;
    text-align: center;
    font-weight: 900;
    font-size: 68px;
    line-height: 68px;
    color: var(--white);
  }
  .event-details {
    position: absolute;
    left: 150px; top: 848px;
    display: flex;
    align-items: flex-start;
  }
  .event-time {
    display: flex;
    align-items: flex-start;
    gap: 6px;
    padding-right: 10px;
    border-right: 2px solid var(--white);
    height: 78px;
  }
  .event-time .icon { margin-top: 4px; }
  .time-range {
    font-family: "Bebas Neue", "Arial Narrow", sans-serif;
    font-size: 38px;
    line-height: 36px;
    color: var(--white);
    text-align: right;
  }
  .event-venue {
    display: flex;
    align-items: flex-start;
    gap: 4px;
    padding-left: 20px;
  }
  .venue-text { color: var(--white); font-size: 21px; line-height: 25px; font-weight: 500; }
  .venue-name { color: var(--red); font-weight: 800; font-size: 22px; line-height: 24px; }
  .torn-edge {
    position: absolute;
    left: 0; top: 955px;
    width: 765px; height: 50px;
  }
  .ticket-panel {
    position: absolute;
    left: 0; top: 1000px;
    width: 765px; height: 200px;
    background: var(--white);
  }
  .ticket-link {
    position: absolute;
    left: 0; top: 1028px;
    width: 765px;
    text-align: center;
    font-size: 28px;
    font-weight: 500;
    color: var(--ink);
    word-spacing: 6px;
  }
  .ticket-link .site-name { color: var(--red); font-weight: 800; }
  .price-badge {
    position: absolute;
    left: 145px; top: 1078px;
    width: 476px; height: 88px;
    filter: drop-shadow(0 10px 8px rgba(0,0,0,0.25));
  }
  .price-badge svg { position: absolute; left: 0; top: 0; }
  .seating-label {
    position: absolute;
    left: 16px; top: 8px;
    font-family: "Bebas Neue", "Arial Narrow", sans-serif;
    font-size: 38px;
    line-height: 36px;
    color: var(--white);
  }
  .price {
    position: absolute;
    top: 4px;
    width: 130px;
    text-align: center;
    color: var(--white);
  }
  .price-amount { font-weight: 900; font-size: 54px; line-height: 60px; }
  .price-note { font-weight: 500; font-size: 13px; line-height: 14px; letter-spacing: 0.5px; white-space: nowrap; }
  .price-adult { left: 188px; }
  .price-student { left: 348px; }
  .price-join {
    position: absolute;
    left: 310px; top: 14px;
    width: 30px;
    text-align: center;
    color: var(--white);
    font-family: "Gloock", Georgia, serif;
    font-size: 22px;
    line-height: 60px;
  }
  .price-divider {
    position: absolute;
    left: 324px; width: 2px;
    background: var(--white);
  }
</style>
</head>
<body>
<main class="flyer">
  <div class="concert-photo" role="img" aria-label="Concert crowd with raised hands facing a stage lit in pink and amber lights"></div>

  <h1 class="event-title">Harmony Four<br>Showcase</h1>

  <p class="event-day">SUNDAY</p>
  <p class="event-date">OCT 2, 2022</p>

  <section class="event-details">
    <div class="event-time">
      <svg class="icon" width="26" height="26" viewBox="0 0 26 26" aria-hidden="true">
        <circle cx="13" cy="13" r="11" fill="none" stroke="#fff" stroke-width="2"/>
        <path d="M13 6 V13 L18 16" fill="none" stroke="#fff" stroke-width="2" stroke-linecap="round"/>
      </svg>
      <div class="time-range">2.00P.M.<br>4.00 P.M.</div>
    </div>
    <div class="event-venue">
      <svg class="icon" width="22" height="28" viewBox="0 0 22 28" aria-hidden="true">
        <path d="M11 2 C6 2 3 6 3 10 C3 15 11 22 11 22 C11 22 19 15 19 10 C19 6 16 2 11 2 Z" fill="none" stroke="#fff" stroke-width="1.8"/>
        <circle cx="11" cy="10" r="3" fill="none" stroke="#fff" stroke-width="1.8"/>
        <path d="M3 25 H19" stroke="#fff" stroke-width="1.6" stroke-linecap="round"/>
      </svg>
      <div class="venue-text">
        <div class="venue-name">Brindle9 Alehouse</div>
        413 Marigold Wy #200,<br>Sacramento, CA 95821
      </div>
    </div>
  </section>

  <div class="ticket-panel"></div>
  <svg class="torn-edge" viewBox="0 0 765 50" preserveAspectRatio="none" aria-hidden="true">
    <path fill="#fff" d="M0 26 L18 22 L30 30 L48 20 L62 28 L80 24 L96 34 L112 22 L130 30 L150 18 L166 28 L186 24 L204 34 L222 22 L240 30 L262 20 L280 32 L300 24 L318 36 L334 26 L352 32 L370 20 L390 28 L410 18 L428 30 L446 24 L466 34 L484 22 L502 28 L522 16 L540 30 L560 22 L578 34 L598 24 L616 30 L636 18 L654 28 L672 22 L690 32 L710 20 L728 28 L746 18 L765 24 L765 50 L0 50 Z"/>
  </svg>

  <p class="ticket-link">Tickets: www.<span class="site-name">Ticketwisp</span>.example</p>

  <div class="price-badge">
    <svg width="476" height="88" viewBox="0 0 476 88" aria-hidden="true">
      <defs>
        <linearGradient id="priceRed" x1="0" y1="0" x2="0" y2="1">
          <stop offset="0" stop-color="#f0141c"/>
          <stop offset="1" stop-color="#c9070f"/>
        </linearGradient>
      </defs>
      <rect x="0" y="0" width="200" height="88" rx="8" fill="#000"/>
      <path d="M150 0 H476 V80 Q476 88 468 88 H150 L176 44 Z" fill="#fff"/>
      <path d="M158 0 H468 Q476 0 476 8 V80 Q476 88 468 88 H158 L184 44 Z" fill="url(#priceRed)"/>
    </svg>
    <div class="seating-label">GENERAL<br>SEATING:</div>
    <div class="price price-adult">
      <div class="price-amount">$15</div>
      <div class="price-note">FOR ADULTS</div>
    </div>
    <span class="price-divider" style="top:16px;height:14px"></span>
    <div class="price-join">&amp;</div>
    <span class="price-divider" style="top:58px;height:14px"></span>
    <div class="price price-student">
      <div class="price-amount">$10</div>
      <div class="price-note">FOR STUDENTS</div>
    </div>
  </div>
</main>
</body>
</html>
```